Startup internet service provider needs a good facebook ad

Looking for a catchy facebook ad to launch our internet service in Parker, Colorado. Short video or slideshow preferred, still pictures are okay.

https://www.facebook.com/BrimfoxNetworks

www.brimfox-networks.example

Target Market(s)

Parker Colorado

Colors
add136
0255a3

```html
<!DOCTYPE html>
<html lang="en">
<head>
<meta charset="utf-8">
<title>Brimfox Networks – Cover Presentation</title>
<link href="https://fonts.googleapis.com/css2?family=Montserrat:ital,wght@0,400;0,500;0,600;0,800;1,500&family=Oswald:wght@600&family=Roboto:wght@400;500;700&display=swap" rel="stylesheet">
<style>
  :root {
    --brand-green: #add136;
    --brand-blue: #0255a3;
    --navy-deep: #0e3a6b;
    --navy-night: #1a2f4c;
    --ink: #2a2a2a;
    --paper: #ffffff;
    --backdrop: #5f5f5f;
    --ui-grey: #e4e6eb;
    --ui-field: #f0f2f5;
    --ui-text: #050505;
    --ui-muted: #65676b;
    --ui-action: #1b74e4;
    --ui-alert: #e41e3f;
  }
  * { margin: 0; padding: 0; box-sizing: border-box; }
  html, body { width: 1200px; height: 1000px; overflow: hidden; background: var(--paper); }
  .stage { position: relative; width: 1200px; height: 1000px; }
  .svg-defs { position: absolute; width: 0; height: 0; }

  /* Presentation backdrop */
  .backdrop { position: absolute; left: 0; top: 0; width: 1200px; height: 490px; background: var(--backdrop); }

  /* Cover banner component (native 928 × 352) */
  .cover-frame { position: absolute; transform-origin: 0 0; }
  .cover-frame--poster { left: 136px; top: 64px; box-shadow: 5px 7px 9px rgba(0,0,0,.45); }
  .cover-frame--page { left: 182px; top: 541px; transform: scale(0.9009); }
  .cover { position: relative; width: 928px; height: 352px; overflow: hidden; background: var(--navy-night); }
  .cover-shapes { position: absolute; inset: 0; }
  .brand { position: absolute; left: 52px; top: 18px; display: flex; align-items: center; gap: 10px; }
  .brand-dot { width: 46px; height: 46px; border-radius: 50%; background: var(--brand-green); }
  .brand-name { font-family: "Montserrat", sans-serif; font-weight: 500; font-size: 23px; color: var(--brand-blue); }
  .headline {
    position: absolute; left: 50px; top: 80px;
    font-family: "Montserrat", sans-serif; font-weight: 800; font-size: 38px; line-height: 1;
    color: var(--navy-deep); letter-spacing: -0.5px;
  }
  .headline .accent { color: var(--brand-green); }
  .subhead {
    position: absolute; left: 50px; top: 124px;
    font-family: "Oswald", sans-serif; font-weight: 600; font-size: 30px; line-height: 1;
    color: var(--ink); letter-spacing: 0.1px;
  }
  .tagline {
    position: absolute; left: 52px; top: 168px;
    font-family: "Montserrat", sans-serif; font-weight: 600; font-size: 18.5px; line-height: 1;
    color: var(--ink); letter-spacing: -0.2px;
  }
  .contacts {
    position: absolute; left: 52px; top: 260px; list-style: none;
    font-family: "Montserrat", sans-serif; font-weight: 400; font-size: 15px; color: var(--paper);
  }
  .contacts li { display: flex; align-items: center; gap: 11px; height: 26px; }
  .contacts .icon { width: 20px; height: 20px; flex: none; }
  .contacts em { font-style: italic; font-weight: 500; color: var(--brand-green); }

  /* Social page preview */
  .topbar {
    position: absolute; left: 0; top: 492px; width: 1200px; height: 49px;
    background: var(--paper); border-bottom: 1px solid #dadde1;
    font-family: "Roboto", sans-serif;
  }
  .topbar-mark { position: absolute; left: 14px; top: 6px; width: 36px; height: 36px; border-radius: 50%; background: var(--ui-action); }
  .search {
    position: absolute; left: 58px; top: 502px; width: 248px; height: 34px; border-radius: 17px;
    background: var(--ui-field); display: flex; align-items: center; gap: 7px; padding-left: 11px;
    font-family: "Roboto", sans-serif; font-size: 14px; color: var(--ui-muted);
  }
  .nav-tab { position: absolute; top: 506px; width: 24px; height: 24px; }
  .nav-badge {
    position: absolute; top: 500px; height: 16px; min-width: 16px; padding: 0 4px; border-radius: 8px;
    background: var(--ui-alert); color: var(--paper); border: 1.5px solid var(--paper);
    font-family: "Roboto", sans-serif; font-weight: 700; font-size: 10px; line-height: 13px; text-align: center;
  }
  .round-btn {
    position: absolute; top: 501px; width: 36px; height: 36px; border-radius: 50%;
    background: var(--ui-grey); display: flex; align-items: center; justify-content: center;
  }
  .cover-sides {
    position: absolute; top: 541px; width: 182px; height: 317px;
    background: linear-gradient(180deg, #2f2f2f 0%, #8a8a8a 45%, #e8e8e8 80%, #ffffff 100%);
  }
  .cover-sides--left { left: 0; }
  .cover-sides--right { left: 1018px; }
  .profile-avatar {
    position: absolute; left: 210px; top: 842px; width: 126px; height: 126px; border-radius: 50%;
    background: var(--brand-green); border: 4px solid var(--paper);
  }
  .page-title {
    position: absolute; left: 357px; top: 883px;
    font-family: "Roboto", sans-serif; font-weight: 700; font-size: 24px; color: var(--ui-text);
  }
  .page-meta {
    position: absolute; left: 357px; top: 917px; width: 320px;
    font-family: "Roboto", sans-serif; font-size: 14.5px; line-height: 18px; color: var(--ui-muted);
  }
  .shop-btn {
    position: absolute; left: 713px; top: 920px; width: 278px; height: 35px; border-radius: 6px;
    background: var(--ui-action); color: var(--paper);
    display: flex; align-items: center; justify-content: center; gap: 6px;
    font-family: "Roboto", sans-serif; font-weight: 500; font-size: 15px;
  }
  .page-link {
    position: absolute; left: 761px; top: 961px; display: flex; align-items: center; gap: 9px;
    font-family: "Roboto", sans-serif; font-size: 12px; color: var(--ui-muted);
  }
  .page-divider { position: absolute; left: 211px; top: 980px; width: 780px; height: 1px; background: #ced0d4; }
  .tab-pill { position: absolute; top: 992px; height: 20px; border-radius: 6px; background: var(--ui-grey); }
  .edit-fab {
    position: absolute; left: 1144px; top: 944px; width: 42px; height: 42px; border-radius: 50%;
    background: var(--paper); box-shadow: 0 2px 8px rgba(0,0,0,.2);
    display: flex; align-items: center; justify-content: center;
  }
</style>
</head>
<body>
<main class="stage">
  <svg class="svg-defs" aria-hidden="true">
    <defs>
      <linearGradient id="family-tones" x1="0" y1="0" x2="1" y2="1">
        <stop offset="0" stop-color="#d9d4c8"/>
        <stop offset="0.45" stop-color="#b48a70"/>
        <stop offset="1" stop-color="#8a7a66"/>
      </linearGradient>
      <linearGradient id="table-tones" x1="0" y1="0" x2="1" y2="1">
        <stop offset="0" stop-color="#b3743e"/>
        <stop offset="1" stop-color="#7d4b25"/>
      </linearGradient>
      <linearGradient id="night-city" x1="0" y1="0" x2="0" y2="1">
        <stop offset="0" stop-color="#243c5e"/>
        <stop offset="1" stop-color="#15263f"/>
      </linearGradient>
    </defs>
  </svg>

  <div class="backdrop"></div>

  <!-- Standalone cover -->
  <div class="cover-frame cover-frame--poster">
    <section class="cover">
      <svg class="cover-shapes" viewBox="0 0 928 352" width="928" height="352">
        <rect width="928" height="352" fill="url(#night-city)"/>
        <path d="M0 0 H452 C452 140 420 236 260 238 C150 240 60 230 0 214 Z" fill="#ffffff"/>
        <path d="M446 0 H486 C462 110 480 260 664 352 H622 C470 280 428 130 446 0 Z" fill="var(--brand-green)"/>
        <path role="img" aria-label="Photo of a family on a sofa using a laptop and tablet at home"
              d="M486 0 H928 V352 H664 C480 260 462 110 486 0 Z" fill="url(#family-tones)"/>
        <circle cx="538" cy="242" r="71" fill="var(--brand-green)"/>
        <circle role="img" aria-label="Top-down photo of people with laptops and tablets around a wooden table"
                cx="538" cy="242" r="65" fill="url(#table-tones)"/>
      </svg>
      <div class="brand"><span class="brand-dot"></span><span class="brand-name">Brimfox Networks</span></div>
      <h1 class="headline">FAST &amp; <span class="accent">RELIABLE</span></h1>
      <p class="subhead">INTERNET SERVICE DESIGNED</p>
      <p class="tagline">&amp; CATERED TO MEET YOUR NEEDS</p>
      <ul class="contacts">
        <li>
          <svg class="icon" viewBox="0 0 20 20"><circle cx="10" cy="10" r="10" fill="var(--brand-green)"/><rect x="5" y="6.5" width="10" height="7" fill="none" stroke="#1a2f4c" stroke-width="1.3"/><path d="M5 6.5 L10 10.5 L15 6.5" fill="none" stroke="#1a2f4c" stroke-width="1.3"/></svg>
          <span>information@<em>brimfox-networks</em>.example</span>
        </li>
        <li>
          <svg class="icon" viewBox="0 0 20 20"><circle cx="10" cy="10" r="10" fill="var(--brand-green)"/><g fill="none" stroke="#1a2f4c" stroke-width="1.2"><circle cx="10" cy="10" r="5.5"/><ellipse cx="10" cy="10" rx="2.4" ry="5.5"/><path d="M4.5 10 H15.5"/></g></svg>
          <span>www.<em>brimfox-networks</em>.example</span>
        </li>
      </ul>
    </section>
  </div>

  <!-- Page preview: top bar -->
  <header class="topbar"><span class="topbar-mark"></span></header>
  <div class="search">
    <svg width="16" height="16" viewBox="0 0 16 16"><circle cx="6.5" cy="6.5" r="5" fill="none" stroke="#65676b" stroke-width="1.6"/><path d="M10.3 10.3 L14.5 14.5" stroke="#65676b" stroke-width="1.6"/></svg>
    <span>Search Friendspace</span>
  </div>
  <svg class="nav-tab" style="left:375px" viewBox="0 0 24 24"><path d="M3 11 L12 3 L21 11 V21 H15 V14 H9 V21 H3 Z" fill="none" stroke="#65676b" stroke-width="1.6" stroke-linejoin="round"/></svg>
  <svg class="nav-tab" style="left:481px" viewBox="0 0 24 24"><rect x="3" y="5" width="18" height="14" rx="3" fill="none" stroke="#65676b" stroke-width="1.6"/><path d="M10 9 L15 12 L10 15 Z" fill="#65676b"/></svg>
  <span class="nav-badge" style="left:499px">9+</span>
  <svg class="nav-tab" style="left:589px" viewBox="0 0 24 24"><path d="M4 4 H20 L21 9 H3 Z M5 9 V20 H19 V9 M10 20 V14 H14 V20" fill="none" stroke="#65676b" stroke-width="1.6" stroke-linejoin="round"/></svg>
  <svg class="nav-tab" style="left:695px" viewBox="0 0 24 24"><circle cx="12" cy="12" r="10" fill="none" stroke="#65676b" stroke-width="1.6"/><circle cx="12" cy="10" r="2.2" fill="#65676b"/><circle cx="7.5" cy="11" r="1.7" fill="#65676b"/><circle cx="16.5" cy="11" r="1.7" fill="#65676b"/><path d="M8.5 17 C9 13.5 15 13.5 15.5 17 Z" fill="#65676b"/></svg>
  <span class="nav-badge" style="left:713px">2</span>
  <svg class="nav-tab" style="left:803px" viewBox="0 0 24 24"><rect x="4" y="4" width="16" height="16" rx="2" fill="none" stroke="#65676b" stroke-width="1.6"/><path d="M4 10 H14 V20" fill="none" stroke="#65676b" stroke-width="1.6"/></svg>
  <span class="round-btn" style="left:1022px"><svg width="16" height="16" viewBox="0 0 16 16"><path d="M8 2 V14 M2 8 H14" stroke="#050505" stroke-width="2"/></svg></span>
  <span class="round-btn" style="left:1065px"><svg width="18" height="18" viewBox="0 0 18 18"><rect x="2" y="3" width="14" height="10" rx="3" fill="#050505"/><path d="M5 13 L5 16 L9 13 Z" fill="#050505"/></svg></span>
  <span class="round-btn" style="left:1108px"><svg width="18" height="18" viewBox="0 0 18 18"><path d="M4 13 V8 A5 5 0 0 1 14 8 V13 L15.5 14.5 H2.5 Z" fill="#050505"/><circle cx="9" cy="16" r="1.6" fill="#050505"/></svg></span>
  <span class="round-btn" style="left:1150px"><svg width="14" height="14" viewBox="0 0 14 14"><path d="M2 4.5 L12 4.5 L7 10 Z" fill="#050505"/></svg></span>

  <!-- Page preview: cover -->
  <div class="cover-sides cover-sides--left"></div>
  <div class="cover-sides cover-sides--right"></div>
  <div class="cover-frame cover-frame--page">
    <section class="cover">
      <svg class="cover-shapes" viewBox="0 0 928 352" width="928" height="352">
        <rect width="928" height="352" fill="url(#night-city)"/>
        <path d="M0 0 H452 C452 140 420 236 260 238 C150 240 60 230 0 214 Z" fill="#ffffff"/>
        <path d="M446 0 H486 C462 110 480 260 664 352 H622 C470 280 428 130 446 0 Z" fill="var(--brand-green)"/>
        <path role="img" aria-label="Photo of a family on a sofa using a laptop and tablet at home"
              d="M486 0 H928 V352 H664 C480 260 462 110 486 0 Z" fill="url(#family-tones)"/>
        <circle cx="538" cy="242" r="71" fill="var(--brand-green)"/>
        <circle role="img" aria-label="Top-down photo of people with laptops and tablets around a wooden table"
                cx="538" cy="242" r="65" fill="url(#table-tones)"/>
      </svg>
      <div class="brand"><span class="brand-dot"></span><span class="brand-name">Brimfox Networks</span></div>
      <h2 class="headline">FAST &amp; <span class="accent">RELIABLE</span></h2>
      <p class="subhead">INTERNET SERVICE DESIGNED</p>
      <p class="tagline">&amp; CATERED TO MEET YOUR NEEDS</p>
      <ul class="contacts">
        <li>
          <svg class="icon" viewBox="0 0 20 20"><circle cx="10" cy="10" r="10" fill="var(--brand-green)"/><rect x="5" y="6.5" width="10" height="7" fill="none" stroke="#1a2f4c" stroke-width="1.3"/><path d="M5 6.5 L10 10.5 L15 6.5" fill="none" stroke="#1a2f4c" stroke-width="1.3"/></svg>
          <span>information@<em>brimfox-networks</em>.example</span>
        </li>
        <li>
          <svg class="icon" viewBox="0 0 20 20"><circle cx="10" cy="10" r="10" fill="var(--brand-green)"/><g fill="none" stroke="#1a2f4c" stroke-width="1.2"><circle cx="10" cy="10" r="5.5"/><ellipse cx="10" cy="10" rx="2.4" ry="5.5"/><path d="M4.5 10 H15.5"/></g></svg>
          <span>www.<em>brimfox-networks</em>.example</span>
        </li>
      </ul>
    </section>
  </div>

  <!-- Page preview: profile header -->
  <span class="profile-avatar"></span>
  <p class="page-title">Brimfox Networks</p>
  <p class="page-meta">@BrimfoxNetworks · Internet Service Provider</p>
  <span class="shop-btn">
    <svg width="15" height="15" viewBox="0 0 15 15"><path d="M4.5 5 V4 A3 3 0 0 1 10.5 4 V5" fill="none" stroke="#fff" stroke-width="1.5"/><rect x="1.5" y="5" width="12" height="9" rx="2" fill="#fff"/></svg>
    Shop Now
  </span>
  <span class="page-link">
    <svg width="14" height="14" viewBox="0 0 14 14"><path d="M6 2 H2 V12 H12 V8 M8 2 H12 V6 M12 2 L6.5 7.5" fill="none" stroke="#65676b" stroke-width="1.4"/></svg>
    brimfox-networks.example
  </span>
  <div class="page-divider"></div>
  <span class="tab-pill" style="left:676px;width:113px"></span>
  <span class="tab-pill" style="left:797px;width:93px"></span>
  <span class="tab-pill" style="left:898px;width:42px"></span>
  <span class="tab-pill" style="left:948px;width:42px"></span>
  <span class="edit-fab"><svg width="18" height="18" viewBox="0 0 18 18"><rect x="2" y="3" width="12" height="13" rx="2" fill="none" stroke="#050505" stroke-width="1.6"/><path d="M8 10 L15 3 L16.5 4.5 L9.5 11.5 L7.5 12 Z" fill="#050505"/></svg></span>
</main>
</body>
</html>
```